Business Card Design Project

We require a professional business card designed for our consulting organisation that has the same theme and colours as our logo except for the grey.

Colours on the front should predominately be white however some reference to our logo colours except for the grey.

The back of the card should be have background colour that aligns with our logo colour.

Layout, style and design is up to the designer. So send through your designs

Details are attached in the word document project brief.

Target Market(s)

Target market are large corporate organisations

Industry/Entity Type

Business

Requirements
Must have
• Content on the front must have:

Dean Halvorsen
Managing Director

P: 0417 285 394
E: Dean@brevolinkpartners.com
W: www.brevolinkpartners.com

Content on the back must have the words:
Alliances
Placement
Training
Support

Design Colours
Must align to our logo

```html
<!DOCTYPE html>
<html lang="en">
<head>
<meta charset="utf-8">
<title>Brevolink Partners – Business Card</title>
<link rel="stylesheet" href="https://fonts.googleapis.com/css2?family=Arimo:wght@400;700&family=Michroma&family=Montserrat:wght@600&display=swap">
<style>
  :root {
    --page: #e6e8eb;
    --card: #ffffff;
    --blue: #1a6fbd;
    --blue-light: #2d8fd2;
    --grey: #555557;
    --grey-soft: #6b6b6d;
  }
  * { margin: 0; padding: 0; box-sizing: border-box; }
  html, body {
    width: 1200px; height: 1000px; overflow: hidden;
    background: var(--page);
    font-family: "Arimo", Arial, sans-serif;
  }
  .canvas { position: relative; width: 1200px; height: 1000px; }
  .card {
    position: absolute; left: 193px; width: 770px; height: 420px;
    background: var(--card); overflow: hidden;
    box-shadow: 0 4px 14px rgba(0,0,0,.18);
  }
  .card--front { top: 60px; }
  .card--back { top: 530px; }

  .brand { position: absolute; display: flex; align-items: center; }
  .brand__mark { background: var(--blue); flex: none; }
  .brand__name {
    font-family: "Montserrat", sans-serif; font-weight: 600;
    color: var(--blue); line-height: 1.02;
  }
  .card--front .brand { left: 150px; top: 150px; gap: 28px; }
  .card--front .brand__mark { width: 96px; height: 96px; }
  .card--front .brand__name { font-size: 50px; }
  .card--back .brand { left: 22px; top: 28px; gap: 16px; }
  .card--back .brand__mark { width: 58px; height: 58px; }
  .card--back .brand__name { font-size: 31px; }

  .services {
    position: absolute; left: 0; right: 0; top: 333px; height: 37px;
    background: var(--blue);
    display: flex; align-items: center; justify-content: center; gap: 24px;
    font-family: "Michroma", sans-serif; font-size: 16px; letter-spacing: 3.6px;
    color: #fff;
  }

  .person__marker { position: absolute; left: 0; top: 220px; }
  .person__name {
    position: absolute; left: 34px; top: 220px;
    font-size: 30px; font-weight: 700; color: var(--blue-light);
  }
  .person__name .surname { color: var(--blue); }
  .person__role {
    position: absolute; left: 34px; top: 254px;
    font-size: 11px; color: var(--grey); letter-spacing: .3px;
  }
  .divider {
    position: absolute; left: 34px; top: 282px; width: 313px; height: 1px;
    background: var(--blue-light);
  }
  .contact { position: absolute; top: 305px; font-size: 11px; color: var(--blue); line-height: 1.3; }
  .contact dt { font-weight: 700; }
  .contact dd { letter-spacing: .6px; }
  .contact--phone { left: 46px; }
  .contact--email { left: 158px; }
  .contact--email dd { letter-spacing: 0; }

  .accent { position: absolute; right: -120px; top: 70px; }

  .website {
    position: absolute; right: 15px; top: 395px;
    font-size: 12px; letter-spacing: 3.2px; color: var(--blue); text-transform: uppercase;
  }
  .base-rule { position: absolute; left: 0; right: 0; bottom: 0; height: 7px; background: var(--blue); }
</style>
</head>
<body>
<main class="canvas">
  <section class="card card--front">
    <div class="brand">
      <span class="brand__mark"></span>
      <span class="brand__name">Brevolink<br>Partners</span>
    </div>
    <div class="services">
      <span>ALLIANCES</span><span>PLACEMENT</span><span>TRAINING</span><span>SUPPORT</span>
    </div>
  </section>

  <section class="card card--back">
    <div class="brand">
      <span class="brand__mark"></span>
      <span class="brand__name">Brevolink<br>Partners</span>
    </div>

    <svg class="person__marker" width="20" height="36" viewBox="0 0 20 36" aria-hidden="true">
      <polygon points="0,0 20,18 0,36" fill="var(--blue)"/>
    </svg>
    <p class="person__name">Dean <span class="surname">Halvorsen</span></p>
    <p class="person__role">MANAGING DIRECTOR</p>
    <div class="divider"></div>

    <dl class="contact contact--phone"><dt>Phone:</dt><dd>0417 285 394</dd></dl>
    <dl class="contact contact--email"><dt>Email:</dt><dd>Dean@brevolinkpartners.com</dd></dl>

    <svg class="accent" width="310" height="310" viewBox="0 0 310 310" aria-hidden="true">
      <circle cx="155" cy="155" r="150" fill="var(--blue-light)"/>
    </svg>

    <p class="website">www.brevolinkpartners.com</p>
    <div class="base-rule"></div>
  </section>
</main>
</body>
</html>
```